Design Cover for Catalog and theme pages to match cover design for continuity

I need a catalog cover for our new catalog and have it flow through the pages uniting the design together. Most the hardest work is complete however it needs a designers touch to bring it all together. The attached files include the catalog with products images data and logos. We have more assets however with the 100MB limit we are unable to upload to many more. For additional images you can pull them from our website www.brenvoxa.example.

Target Market(s)

Tradesmen and trades women who work in the Electrical and Industrial Automation spaces.

Industry/Entity Type

Industrial

Font styles to use
Sans Serif

Colors
3176b5
0555a3
85cae6

Requirements
Must have
• Complete cover design
• Must also have cover theme flow through remaining pages
Nice to have
• Header and Footer on each page
• Index on cover with page reference
Should not have
• This is not a redesign of the whole catalog, please don't drastically change the pages or any of the data in the tables.

```html
<!DOCTYPE html>
<html lang="en">
<head>
<meta charset="utf-8">
<title>Brenvoxa Product Catalog – Cover and Theme Pages</title>
<link href="https://fonts.googleapis.com/css2?family=Bebas+Neue&family=Roboto+Condensed:wght@400;700&display=swap" rel="stylesheet">
<style>
  :root {
    --brand-blue: #3176b5;
    --deep-blue: #0555a3;
    --sky-blue: #85cae6;
    --frame-blue: #3566c4;
    --stage: #2f5fb8;
    --cover-top: #62aee3;
    --cover-bottom: #30379a;
    --ink: #1b1b1b;
    --rule: #8a8a8a;
    --head-grey: #9a9a9a;
    --photo-grey: #c9cdd1;
    --paper: #ffffff;
  }
  * { box-sizing: border-box; margin: 0; padding: 0; }
  html, body { width: 1200px; height: 1200px; overflow: hidden; }
  body { background: var(--stage); font-family: "Roboto Condensed", sans-serif; color: var(--ink); position: relative; }
  .abs { position: absolute; }

  .spread { left: 37px; top: 75px; width: 1126px; height: 728px; background: var(--paper); }
  .cover-panel { left: 25px; top: 25px; width: 514px; height: 678px;
    background: linear-gradient(180deg, var(--cover-top) 0%, #4d8fd6 30%, #3a59b3 65%, var(--cover-bottom) 100%); }
  .cover-tagline { left: 0; width: 514px; top: 385px; text-align: center; color: #fff;
    font-family: "Bebas Neue", sans-serif; font-size: 35px; line-height: 30.5px; letter-spacing: -0.3px; }
  .brand { display: flex; align-items: center; gap: 3px; font-family: "Roboto Condensed", sans-serif; font-weight: 700; }
  .brand-dot { width: 12px; height: 12px; border-radius: 50%; background: currentColor; }
  .cover-brand { left: 0; width: 514px; top: 605px; justify-content: center; color: #fff; font-size: 20px; }

  .page-band-top { left: 563px; top: 25px; width: 515px; height: 25px; background: var(--frame-blue); }
  .page-band-side { left: 1077px; top: 25px; width: 25px; height: 703px; background: var(--frame-blue); }
  .page-brand { left: 985px; top: 29px; color: #fff; font-size: 12px; }

  .section-title { font-family: "Bebas Neue", sans-serif; font-size: 20px; line-height: 18px; color: var(--ink); }
  .title-mark { width: 58px; height: 50px; border-left: 4px solid var(--frame-blue); border-top: 4px solid var(--frame-blue); }
  .title-mark::after { content: ""; position: absolute; left: 4px; top: 4px; width: 50px; height: 40px;
    border-left: 3px solid var(--sky-blue); border-top: 3px solid var(--sky-blue); }

  .badge { background: var(--deep-blue); border-radius: 50%; }
  .badge-square { background: #111; border-radius: 3px; }

  .photo { background: linear-gradient(160deg, #e6e8ea 0%, var(--photo-grey) 55%, #a9aeb3 100%); border-radius: 4px; }

  table.spec { border-collapse: collapse; font-size: 7.2px; text-align: center; background: #fff; }
  table.spec th, table.spec td { border: 0.8px solid var(--rule); padding: 0 2px; font-weight: 400; white-space: nowrap; }
  table.spec th { line-height: 8px; }
  table.spec .sub { background: var(--head-grey); color: #f0f0f0; font-size: 6.5px; }
  table.attrs td.key { background: var(--head-grey); color: #eee; }
  .rule-line { height: 1px; background: #9c9c9c; }

  .thumb { top: 866px; height: 239px; background: var(--paper); }
  .thumb-frame { position: absolute; left: 12px; top: 10px; right: 12px; bottom: 0;
    border-top: 8px solid var(--frame-blue); border-left: 8px solid var(--frame-blue); border-right: 8px solid var(--frame-blue); }
  .thumb-grid { position: absolute; left: 20px; top: 26px; right: 20px; bottom: 6px;
    display: grid; grid-template-columns: 1fr 1fr; gap: 6px 14px; }
  .thumb-block { display: flex; flex-direction: column; gap: 3px; }
  .thumb-title { font-family: "Bebas Neue", sans-serif; font-size: 7px; line-height: 7px; border-left: 2px solid var(--frame-blue); padding-left: 3px; white-space: nowrap; }
  .thumb-row { display: flex; gap: 4px; flex: 1; }
  .thumb-photo { flex: 1.2; background: linear-gradient(160deg, #e4e6e8, #b3b8bd); border-radius: 2px; }
  .thumb-table { flex: 1; background: repeating-linear-gradient(180deg, #fff 0 4px, #b8b8b8 4px 5px); border: 0.6px solid #999; }
</style>
</head>
<body>
  <section class="spread abs">
    <div class="cover-panel abs">
      <p class="cover-tagline abs">To build efficiently,<br>we take pride in<br>providing high<br>quality and durable<br>solutions to<br>the market.</p>
      <div class="brand cover-brand abs"><span>Brenvoxa</span><span class="brand-dot"></span></div>
    </div>

    <div class="page-band-top abs"></div>
    <div class="page-band-side abs"></div>
    <div class="brand page-brand abs"><span>Brenvoxa</span><span class="brand-dot" style="width:8px;height:8px"></span></div>

    <div class="title-mark abs" style="left:593px;top:80px"></div>
    <h2 class="section-title abs" style="left:614px;top:98px">Aluminum<br>Terminal<br>Enclosures</h2>
    <div class="photo abs" role="img" aria-label="Group of grey cast aluminum terminal enclosures with terminal blocks" style="left:712px;top:65px;width:245px;height:160px"></div>
    <div class="badge abs" style="left:974px;top:75px;width:36px;height:36px"></div>
    <div class="badge-square abs" style="left:1026px;top:80px;width:30px;height:28px"></div>

    <table class="spec abs" style="left:635px;top:241px;width:242px">
      <tr><th rowspan="2" style="height:26px">NO. OF CIRCUITS</th><th rowspan="2">OUTSIDE DIM.<br>L x W x H</th><th rowspan="2">SHPG.<br>WEIGHT</th><th>MODEL NO.</th></tr>
      <tr><th class="sub">Gray Cast Aluminum</th></tr>
      <tr style="height:16px"><td>4 Circuits</td><td>61 x 71 x 48</td><td>0.53 lbs</td><td>BX-CA-4T</td></tr>
      <tr style="height:16px"><td>6 Circuits</td><td>93 x 70 x 52</td><td>0.62 lbs</td><td>BX-CA-6T</td></tr>
      <tr style="height:16px"><td>10 Circuits</td><td>128 x 70 x 52</td><td>0.88 lbs</td><td>BX-CA-10T</td></tr>
      <tr style="height:16px"><td>12 Circuits</td><td>110 x 110 x 52</td><td>1.1 lbs</td><td>BX-CA-12T</td></tr>
      <tr style="height:16px"><td>15 Circuits</td><td>172 x 70 x 55</td><td>1.32 lbs</td><td>BX-CA-15T</td></tr>
      <tr style="height:16px"><td>20 Circuits</td><td>145 x 125 x 62</td><td>1.54 lbs</td><td>BX-CA-20T</td></tr>
      <tr style="height:16px"><td>20 Circuits</td><td>265 x 80 x 80</td><td>2.25 lbs</td><td>BX-CA-20TL</td></tr>
      <tr style="height:16px"><td>30 Circuits</td><td>190 x 125 x 80</td><td>2.87 lbs</td><td>BX-CA-30T</td></tr>
      <tr style="height:16px"><td>40 Circuits</td><td>260 x 160 x 90</td><td>5.51 lbs</td><td>BX-CA-40T</td></tr>
      <tr style="height:16px"><td>50 Circuits</td><td>330 x 230 x 120</td><td>11.5 lbs</td><td>BX-CA-50T</td></tr>
    </table>

    <table class="spec attrs abs" style="left:900px;top:241px;width:144px">
      <tr style="height:19px"><td class="key">COLOR(S)</td><td>Gray</td></tr>
      <tr style="height:19px"><td class="key">INGRESS PROTECTION</td><td>IP67 / NEMA 12X</td></tr>
      <tr style="height:19px"><td class="key">MATERIAL</td><td>Cast Aluminum</td></tr>
      <tr style="height:21px"><td class="key">INPUT CURRENT</td><td>15 Ampers</td></tr>
      <tr style="height:19px"><td class="key">RATED FREQUENCY</td><td>60Hz</td></tr>
      <tr style="height:21px"><td class="key">RATED INPUT VOLTAGE</td><td>120 Volts</td></tr>
      <tr style="height:19px"><td class="key">CERTIFYING AGENCY</td><td>Norcert</td></tr>
      <tr style="height:24px"><td class="key">COUNTRIES</td><td>Canada, USA,<br>Germany</td></tr>
      <tr style="height:18px"><td class="key">STANDARDS</td><td>STD 508A</td></tr>
    </table>

    <div class="rule-line abs" style="left:738px;top:450px;width:320px"></div>
    <div class="title-mark abs" style="left:589px;top:440px"></div>
    <h2 class="section-title abs" style="left:609px;top:460px">Project<br>Boxes</h2>
    <div class="badge abs" style="left:998px;top:458px;width:22px;height:22px"></div>
    <div class="badge-square abs" style="left:1025px;top:461px;width:18px;height:17px"></div>
    <div class="photo abs" role="img" aria-label="Grey cast aluminum project boxes with open tops" style="left:585px;top:510px;width:260px;height:135px"></div>

    <table class="spec abs" style="left:868px;top:489px;width:177px">
      <tr><th rowspan="2" style="height:18px">OUTSIDE DIM.<br>L x W x H</th><th rowspan="2">SHPG.<br>WEIGHT</th><th>MODEL NO.</th></tr>
      <tr><th class="sub">Gray Cast Aluminum</th></tr>
      <tr style="height:15.5px"><td>61 x 71 x 48</td><td>0.55 lbs</td><td>BX-CA-P06148</td></tr>
      <tr style="height:15.5px"><td>93 x 70 x 52</td><td>0.59 lbs</td><td>BX-CA-P09352</td></tr>
      <tr style="height:15.5px"><td>128 x 70 x 52</td><td>0.86 lbs</td><td>BX-CA-P12852</td></tr>
      <tr style="height:15.5px"><td>110 x 110 x 52</td><td>1.03 lbs</td><td>BX-CA-P11052</td></tr>
      <tr style="height:15.5px"><td>172 x 70 x 55</td><td>1.21 lbs</td><td>BX-CA-P17255</td></tr>
      <tr style="height:15.5px"><td>145 x 125 x 62</td><td>1.29 lbs</td><td>BX-CA-P14562</td></tr>
      <tr style="height:15.5px"><td>120 x 120 x 80</td><td>1.80 lbs</td><td>BX-CA-P12080</td></tr>
      <tr style="height:15.5px"><td>235 x 80 x 80</td><td>2.23 lbs</td><td>BX-CA-P23580</td></tr>
      <tr style="height:15.5px"><td>190 x 125 x 80</td><td>2.30 lbs</td><td>BX-CA-P19080</td></tr>
      <tr style="height:15.5px"><td>160 x 160 x 90</td><td>2.56 lbs</td><td>BX-CA-P16090</td></tr>
      <tr style="height:15.5px"><td>220 x 125 x 90</td><td>3.01 lbs</td><td>BX-CA-P22090</td></tr>
      <tr style="height:15.5px"><td>260 x 160 x 90</td><td>3.32 lbs</td><td>BX-CA-P26090</td></tr>
    </table>
  </section>

  <section class="thumb abs" style="left:35px;width:369px">
    <div class="thumb-frame"></div>
    <div class="thumb-grid">
      <div class="thumb-block"><h3 class="thumb-title">ABS Terminal Enclosures</h3><div class="thumb-row"><div class="thumb-photo" role="img" aria-label="ABS terminal enclosures"></div><div class="thumb-table"></div></div></div>
      <div class="thumb-block"><h3 class="thumb-title">Wire Connector / DIN Rail</h3><div class="thumb-row"><div class="thumb-photo" role="img" aria-label="Wire connectors and DIN rail"></div><div class="thumb-table"></div></div></div>
      <div class="thumb-block"><div class="thumb-row"><div class="thumb-table"></div><div class="thumb-table"></div></div></div>
      <div class="thumb-block"><h3 class="thumb-title">PVC Connector Box</h3><div class="thumb-row"><div class="thumb-photo" role="img" aria-label="PVC connector box"></div><div class="thumb-table"></div></div></div>
      <div class="thumb-block"><div class="thumb-row"><div class="thumb-table"></div></div></div>
      <div class="thumb-block"><h3 class="thumb-title">Power Distribution</h3><div class="thumb-row"><div class="thumb-photo" role="img" aria-label="Power distribution block"></div><div class="thumb-table"></div></div></div>
    </div>
  </section>

  <section class="thumb abs" style="left:414px;width:368px">
    <div class="thumb-frame"></div>
    <div class="thumb-grid">
      <div class="thumb-block"><h3 class="thumb-title">Ex-Rated Aluminum Enclosures</h3><div class="thumb-row"><div class="thumb-photo" role="img" aria-label="Ex-rated aluminum enclosures"></div><div class="thumb-table"></div></div></div>
      <div class="thumb-block"><h3 class="thumb-title">LED Machine Light</h3><div class="thumb-row"><div class="thumb-photo" role="img" aria-label="LED machine light"></div><div class="thumb-table"></div></div></div>
      <div class="thumb-block"><h3 class="thumb-title">Aluminum Hinge Boxes</h3><div class="thumb-row"><div class="thumb-photo" role="img" aria-label="Aluminum hinge push button boxes"></div><div class="thumb-table"></div></div></div>
      <div class="thumb-block"><div class="thumb-row"><div class="thumb-table"></div><div class="thumb-photo" role="img" aria-label="LED light bars"></div></div></div>
      <div class="thumb-block"><div class="thumb-row"><div class="thumb-table"></div></div></div>
      <div class="thumb-block"><h3 class="thumb-title">Aluminum Profile LED Lamp</h3><div class="thumb-row"><div class="thumb-photo" role="img" aria-label="Aluminum profile LED lamps"></div><div class="thumb-table"></div></div></div>
    </div>
  </section>

  <section class="thumb abs" style="left:796px;width:368px">
    <div class="thumb-frame"></div>
    <div class="thumb-grid">
      <div class="thumb-block"><h3 class="thumb-title">Aluminum Push Button Boxes</h3><div class="thumb-row"><div class="thumb-photo" role="img" aria-label="Aluminum push button boxes"></div><div class="thumb-table"></div></div></div>
      <div class="thumb-block"><h3 class="thumb-title">Earth Bar / DC Terminal Block</h3><div class="thumb-row"><div class="thumb-photo" role="img" aria-label="Earth bars and terminal blocks"></div><div class="thumb-table"></div></div></div>
      <div class="thumb-block"><h3 class="thumb-title">PVC Push Button Boxes</h3><div class="thumb-row"><div class="thumb-photo" role="img" aria-label="Colored PVC push button boxes"></div><div class="thumb-table"></div></div></div>
      <div class="thumb-block"><h3 class="thumb-title">Short Bar</h3><div class="thumb-row"><div class="thumb-photo" role="img" aria-label="Short bars"></div><div class="thumb-table"></div></div></div>
      <div class="thumb-block"><h3 class="thumb-title">Mini Push Button Box</h3><div class="thumb-row"><div class="thumb-photo" role="img" aria-label="Emergency stop push button box"></div><div class="thumb-table"></div></div></div>
      <div class="thumb-block"><h3 class="thumb-title">Cable Glands / Brass Cable Gland</h3><div class="thumb-row"><div class="thumb-photo" role="img" aria-label="Cable glands"></div><div class="thumb-table"></div></div></div>
    </div>
  </section>
</body>
</html>
```